Business Card Design Project for Heron Lending

Hello there,

We are looking for a business card design for our new Heron Lending car financing company. We are looking for a business card that will include:

- An address
- Telephone number and extension
- Employee Name
- Employee Title
- Our logo and name clearly visible

We are including our logo with this writeup, we are looking to convey friendliness, trus and memorability. Colors and everything else is up to you.

Target Market(s)

18-34 year old males and females

Industry/Entity Type

Business

```html
<!DOCTYPE html>
<html lang="en">
<head>
<meta charset="utf-8">
<title>Heron Lending — Business Card</title>
<link rel="stylesheet" href="https://fonts.googleapis.com/css2?family=Open+Sans:wght@400;700&display=swap">
<style>
  :root {
    --page-bg: #eeeeef;
    --card-navy: #053a52;
    --card-ink: #ffffff;
    --card-ink-soft: #d7e2e8;
  }
  * { box-sizing: border-box; margin: 0; padding: 0; }
  html, body {
    width: 1200px;
    height: 675px;
    overflow: hidden;
    background: var(--page-bg);
    font-family: "Open Sans", Arial, sans-serif;
  }
  .stage {
    width: 1200px;
    height: 675px;
    display: flex;
    align-items: center;
    justify-content: center;
    gap: 60px;
  }
  .card {
    width: 525px;
    height: 300px;
    background: var(--card-navy);
    color: var(--card-ink);
    position: relative;
    overflow: hidden;
  }
  .brand-mark {
    flex: none;
    border-radius: 50%;
    background: var(--card-ink);
  }
  .brand-name {
    font-weight: 700;
    text-transform: uppercase;
    color: var(--card-ink);
    letter-spacing: 0.06em;
    white-space: nowrap;
  }

  /* Back of card: logo block centred, filling the middle of the card */
  .card-back {
    display: flex;
    align-items: center;
    justify-content: center;
  }
  .card-back .brand {
    display: flex;
    align-items: center;
    gap: 22px;
  }
  .card-back .brand-mark {
    width: 96px;
    height: 96px;
  }
  .card-back .brand-name {
    font-size: 30px;
    line-height: 1.1;
  }

  /* Front of card: logo block left, contact details right */
  .card-front .brand {
    position: absolute;
    left: 30px;
    top: 74px;
    width: 220px;
    display: flex;
    flex-direction: column;
    align-items: center;
    gap: 16px;
  }
  .card-front .brand-mark {
    width: 92px;
    height: 92px;
  }
  .card-front .brand-name {
    font-size: 24px;
    line-height: 1.1;
  }
  .contact {
    position: absolute;
    left: 288px;
    top: 66px;
  }
  .person-name {
    font-weight: 700;
    font-size: 15px;
    line-height: 1.2;
  }
  .person-title {
    font-size: 11px;
    color: var(--card-ink-soft);
    margin: 2px 0 0 12px;
  }
  .details {
    list-style: none;
    margin: 26px 0 0 40px;
    font-size: 12.5px;
    line-height: 1.25;
    color: var(--card-ink-soft);
  }
  .details li {
    display: flex;
    align-items: flex-start;
    gap: 8px;
    margin-bottom: 3px;
  }
  .details svg {
    flex: none;
    width: 12px;
    height: 12px;
    margin-top: 2px;
    fill: var(--card-ink);
  }
</style>
</head>
<body>
  <main class="stage">
    <section class="card card-back" aria-label="Card back">
      <div class="brand">
        <span class="brand-mark" aria-hidden="true"></span>
        <span class="brand-name">Heron Lending</span>
      </div>
    </section>

    <section class="card card-front" aria-label="Card front">
      <div class="brand">
        <span class="brand-mark" aria-hidden="true"></span>
        <span class="brand-name">Heron Lending</span>
      </div>
      <div class="contact">
        <p class="person-name">Your Long Name</p>
        <p class="person-title">Your Title</p>
        <ul class="details">
          <li>
            <svg viewBox="0 0 24 24" aria-hidden="true"><path d="M2 8c3-4 17-4 20 0l-2 3-4-1V8c-2-1-6-1-8 0v2l-4 1zM6 13h12l2 8H4z"/></svg>
            <span>00,00,00,0000</span>
          </li>
          <li>
            <svg viewBox="0 0 24 24" aria-hidden="true"><path d="M12 1a8 8 0 0 0-8 8c0 6 8 14 8 14s8-8 8-14a8 8 0 0 0-8-8zm0 11a3 3 0 1 1 0-6 3 3 0 0 1 0 6z"/></svg>
            <span>Your Commercial<br>or office address</span>
          </li>
        </ul>
      </div>
    </section>
  </main>
</body>
</html>
```